Clothing Brand E-Commerce Website Design

We would like you to provide an ecommerce design template in layered PSD for our clothing/fashion brand website called "TrelWick".
We want the site to have a simple but sleek design similar to the following sites:
http://www.pivorane.com/
http://corvatelle.com/
http://www.dulvenor.com/
We want it to look stunning and blow the example sites out of the water. For color scheme, please use your imagination and try to impress us with your creativity.
We like teal and beige pink, with teal dominant.
Teal #7AFFFF / #46C6C6
Beige/pink #FF7B7C / #C74646
We want you to develop the design for 3 pages:
1) Home Page
Samples:
http://www.pivorane.com/
http://corvatelle.com/
http://www.dulvenor.com/
2) Products List Page (e.g., lists all "Dresses" when category is selected)
http://www.pivorane.com/shop/casual-dresses
http://www.dulvenor.com/index.php?main_page=index&cPath=3
http://corvatelle.com/modest-dresses.html
http://www.quillmarsh.com/Product/Category.aspx?br=q47&category=dress_maxi
3) Product Detail Page (e.g., individual product page with "Add to Cart")
http://www.pivorane.com/shop/dresses/lumen-fern-dress
http://corvatelle.com/modest-dresses/modest-dress-tova.html
http://www.dulvenor.com/index.php?main_page=product_info&cPath=3&products_id=297
Industry/Entity Type
Fashion

```html
<!DOCTYPE html>
<html lang="en">
<head>
<meta charset="utf-8">
<title>TrelWick — Home</title>
<link rel="stylesheet" href="https://fonts.googleapis.com/css2?family=Raleway:wght@400;600;700&display=swap">
<style>
:root{
  --teal:#7affff;
  --teal-deep:#46c6c6;
  --ink:#1d1d1d;
  --bar:#2b2b2b;
  --paper:#ffffff;
  --mist:#e9e9e9;
  --text:#555;
}
*{box-sizing:border-box;margin:0;padding:0}
html,body{width:1200px;height:2892px;overflow:hidden}
body{font-family:"Raleway",sans-serif;color:var(--ink);background:var(--paper);position:relative}
.abs{position:absolute}
.photo{position:absolute}

/* header */
.topbar{left:0;top:0;width:1200px;height:52px;background:rgba(40,40,40,.55);display:flex;align-items:center;justify-content:space-between;padding:0 180px;z-index:2}
.topbar nav{display:flex;gap:28px;font-size:11px;letter-spacing:2px;color:#eee}
.brand{font-size:22px;font-weight:600;color:#fff;letter-spacing:1px}
.hero{left:0;top:0;width:1200px;height:520px;background:radial-gradient(ellipse at 50% 55%,#3a3030 0 14%,#bdbdbd 30%,#d8d8d8 60%,#c9c9c9 100%)}
.arrow{width:26px;height:26px;background:var(--teal-deep);display:flex;align-items:center;justify-content:center}
.arrow svg{width:12px;height:12px}

/* shop */
.shop{left:0;top:520px;width:1200px;height:680px;background:var(--teal)}
.section-bar{left:180px;width:840px;height:30px;background:var(--teal-deep);color:#fff;font-weight:700;letter-spacing:3px;font-size:15px;display:flex;align-items:center;justify-content:center}
.shop .section-bar{top:14px}
.grid{left:218px;width:764px;display:grid;grid-template-columns:repeat(6,112px);column-gap:18px}
.card{background:#fff;height:240px;padding:6px}
.card .pic{height:170px}
.card h4{font-size:9px;font-weight:700;margin-top:6px}
.card p{font-size:8px;color:var(--text);margin-top:2px}
.card .price{font-size:9px;font-weight:600;margin-top:3px;color:var(--ink)}

/* banners */
.gown{left:0;top:1200px;width:1200px;height:450px;background:linear-gradient(100deg,#3a2a12 0%,#8a6a30 35%,#e8e2d6 55%,#b59a62 75%,#4a3516 100%)}
.story{left:0;top:1650px;width:1200px;height:240px;background:#fbfbfb}
.story .brand{color:var(--ink);font-size:30px;left:340px;top:80px;position:absolute}
.story h3{position:absolute;left:570px;top:42px;font-size:15px;letter-spacing:2px;font-weight:700}
.story p{position:absolute;left:570px;top:72px;width:380px;font-size:10px;line-height:1.6;color:var(--text)}
.blush{left:0;top:1890px;width:1200px;height:450px;background:linear-gradient(90deg,#4a1010 0%,#2c3a22 25%,#e7c9c0 45%,#f0d8d0 55%,#2a3a26 75%,#1e2a1c 100%)}

/* about */
.about{left:0;top:2340px;width:1200px;height:420px;background:var(--mist)}
.about .section-bar{top:18px;background:var(--bar)}
.about h5{font-size:14px;font-weight:700;letter-spacing:1px}
.about p{font-size:9px;line-height:1.55;color:var(--text);margin-top:6px}

/* footer */
.footer{left:0;top:2760px;width:1200px;height:132px;background:#fff}
.links{left:180px;top:12px;display:grid;grid-template-columns:repeat(4,150px);row-gap:10px;font-size:9px;letter-spacing:1px;color:var(--text)}
.news{left:780px;top:12px;width:240px;height:60px;background:var(--bar);padding:8px}
.news span{font-size:8px;letter-spacing:1px;color:#fff}
.news .field{margin-top:10px;display:flex}
.news .field i{flex:1;height:18px;background:#fff}
.news .field b{width:24px;height:18px;background:var(--teal-deep)}
.footer .brand{position:absolute;left:180px;top:98px;color:var(--ink);font-size:16px}
.copy{left:360px;top:104px;font-size:8px;color:#888}
.totop{left:980px;top:100px}
</style>
</head>
<body>

<div class="abs hero" role="img" aria-label="Hero photo of a model in a black lace dress against a pale floral backdrop"></div>
<header class="abs topbar">
  <nav><span>HOME</span><span>ABOUT</span><span>SHOP</span></nav>
  <div class="brand">TrelWick</div>
  <nav><span>BLOG</span><span>CART</span></nav>
</header>
<div class="abs arrow" style="left:180px;top:297px"><svg viewBox="0 0 12 12"><path d="M8 1 3 6l5 5" stroke="#fff" stroke-width="2" fill="none"/></svg></div>
<div class="abs arrow" style="left:994px;top:297px"><svg viewBox="0 0 12 12"><path d="M4 1l5 5-5 5" stroke="#fff" stroke-width="2" fill="none"/></svg></div>

<section class="abs shop">
  <div class="abs section-bar">SHOP</div>
  <div class="abs arrow" style="left:180px;top:150px"><svg viewBox="0 0 12 12"><path d="M8 1 3 6l5 5" stroke="#fff" stroke-width="2" fill="none"/></svg></div>
  <div class="abs arrow" style="left:994px;top:150px"><svg viewBox="0 0 12 12"><path d="M4 1l5 5-5 5" stroke="#fff" stroke-width="2" fill="none"/></svg></div>
  <div class="abs arrow" style="left:180px;top:420px"><svg viewBox="0 0 12 12"><path d="M8 1 3 6l5 5" stroke="#fff" stroke-width="2" fill="none"/></svg></div>
  <div class="abs arrow" style="left:994px;top:420px"><svg viewBox="0 0 12 12"><path d="M4 1l5 5-5 5" stroke="#fff" stroke-width="2" fill="none"/></svg></div>

  <div class="abs grid" style="top:66px">
    <div class="card"><div class="pic" role="img" aria-label="Printed dress" style="background:linear-gradient(#f4f4f4,#5a4a6a 40%,#3a3048)"></div><h4>QUILLMARSH 21</h4><p>Printed sleeveless day dress</p><div class="price">$24.90</div></div>
    <div class="card"><div class="pic" role="img" aria-label="Striped maxi dress" style="background:linear-gradient(#f4f4f4,#8a8a8a 40%,#4a4a4a)"></div><h4>QUILLMARSH 21</h4><p>Striped jersey maxi dress</p><div class="price">$27.80</div></div>
    <div class="card"><div class="pic" role="img" aria-label="Patterned maxi dress" style="background:linear-gradient(#f4f4f4,#a07a6a 40%,#6a4a40)"></div><h4>QUILLMARSH 21</h4><p>Patterned flowing maxi</p><div class="price">$29.90</div></div>
    <div class="card"><div class="pic" role="img" aria-label="Green maxi dress" style="background:linear-gradient(#f4f4f4,#3a5a4a 40%,#24382e)"></div><h4>QUILLMARSH 21</h4><p>Green halter maxi dress</p><div class="price">$32.80</div></div>
    <div class="card"><div class="pic" role="img" aria-label="Blue floral maxi dress" style="background:linear-gradient(#f4f4f4,#7a90c0 40%,#4a5a8a)"></div><h4>QUILLMARSH 21</h4><p>Blue floral maxi dress</p><div class="price">$29.90</div></div>
    <div class="card"><div class="pic" role="img" aria-label="Navy print dress" style="background:linear-gradient(#f4f4f4,#3a3a5a 40%,#22223a)"></div><h4>QUILLMARSH 21</h4><p>Navy print skater dress</p><div class="price">$22.80</div></div>
  </div>
  <div class="abs grid" style="top:336px">
    <div class="card"><div class="pic" role="img" aria-label="Red patterned dress" style="background:linear-gradient(#f4f4f4,#b0503a 40%,#7a3020)"></div><h4>QUILLMARSH 21</h4><p>Red patterned midi dress</p><div class="price">$26.90</div></div>
    <div class="card"><div class="pic" role="img" aria-label="Plaid dress" style="background:linear-gradient(#f4f4f4,#9a8470 40%,#5a4a3a)"></div><h4>QUILLMARSH 21</h4><p>Plaid long sleeve dress</p><div class="price">$24.80</div></div>
    <div class="card"><div class="pic" role="img" aria-label="Black fitted dress" style="background:linear-gradient(#f4f4f4,#2a2a2a 40%,#111)"></div><h4>QUILLMARSH 21</h4><p>Black fitted knee dress</p><div class="price">$21.90</div></div>
    <div class="card"><div class="pic" role="img" aria-label="Blue print dress" style="background:linear-gradient(#f4f4f4,#4a6a9a 40%,#2a3a5a)"></div><h4>QUILLMARSH 21</h4><p>Blue print shift dress</p><div class="price">$23.80</div></div>
    <div class="card"><div class="pic" role="img" aria-label="White lace dress" style="background:linear-gradient(#f4f4f4,#e6e6e6 40%,#cfcfcf)"></div><h4>QUILLMARSH 21</h4><p>White lace midi dress</p><div class="price">$28.90</div></div>
    <div class="card"><div class="pic" role="img" aria-label="Coral print dress" style="background:linear-gradient(#f4f4f4,#d0704a 40%,#8a4030)"></div><h4>QUILLMARSH 21</h4><p>Coral print sun dress</p><div class="price">$25.80</div></div>
  </div>
</section>

<div class="abs gown" role="img" aria-label="Photo of a white bridal gown in warm golden light"></div>

<section class="abs story">
  <div class="brand">TrelWick</div>
  <h3>NAME AND NAME</h3>
  <p>Lorem ipsum is simply dummy text of the printing and typesetting industry. Lorem ipsum has been the standard dummy text ever since the 1500s, when an unknown printer took a galley of type and scrambled it to make a type specimen book. It has survived not only five centuries, but also the leap into electronic typesetting, remaining essentially unchanged.</p>
</section>

<div class="abs blush" role="img" aria-label="Photo of a model in a blush pink embroidered dress on a red carpet"></div>

<section class="abs about">
  <div class="abs section-bar">ABOUT</div>
  <div class="abs" style="left:180px;top:66px;width:260px">
    <h5>LOREM IPSUM</h5>
    <p>Lorem ipsum is simply dummy text of the printing and typesetting industry. Lorem ipsum has been the standard dummy text ever since the 1500s, when an unknown printer took a galley of type and scrambled it to make a type specimen book.</p>
  </div>
  <div class="photo" style="left:180px;top:196px;width:260px;height:170px;background:linear-gradient(#b8c4cc,#3a7ac0 60%,#2a5a90)" role="img" aria-label="Photo of a model in a blue dress"></div>
  <div class="photo" style="left:470px;top:66px;width:260px;height:300px;background:linear-gradient(#e8e4ee,#b49ad0 55%,#8a70b0)" role="img" aria-label="Photo of a model in a lilac strapless gown"></div>
  <div class="photo" style="left:760px;top:66px;width:260px;height:170px;background:linear-gradient(120deg,#6a4a2a,#c09060 50%,#3a2a1a)" role="img" aria-label="Photo of a woman in an elegant evening look"></div>
  <div class="abs" style="left:760px;top:250px;width:260px">
    <h5>LOREM IPSUM</h5>
    <p>Lorem ipsum is simply dummy text of the printing and typesetting industry. Lorem ipsum has been the standard dummy text ever since the 1500s, when an unknown printer took a galley of type and scrambled it.</p>
  </div>
</section>

<footer class="abs footer">
  <div class="abs links">
    <span>ABOUT US</span><span>PRIVACY POLICY</span><span>ADVANCED SEARCH</span><span>ORDERS &amp; RETURNS</span>
    <span>OUR CLIENTS</span><span>SITE MAP</span><span>CONTACT US</span><span>SHIPPING</span>
    <span>CUSTOMER SERVICE</span><span>SEARCH TERMS</span><span>FOLLOW US</span><span>FAQ</span>
  </div>
  <div class="abs news"><span>JOIN OUR NEWSLETTER</span><div class="field"><i></i><b></b></div></div>
  <div class="brand">TrelWick</div>
  <div class="abs copy">© 2014 TrelWick. All rights reserved. Designed with care.</div>
  <div class="abs arrow totop"><svg viewBox="0 0 12 12"><path d="M1 8l5-5 5 5" stroke="#fff" stroke-width="2" fill="none"/></svg></div>
</footer>

</body>
</html>
```